professional business card design

Business card design. Photos have been uploaded and i am open to the designer choosing which photos to use. Would like the card to be mostyly in a grey scale design with black, whites, silver & grey colours. I have added copy of our flyer as would like on the back side of card our services to be listed. Do not use any bright colurs such as blue red green or yellow. i need to be able to edit the phone number and naem in the final card design submitted.

Target Market(s)

Clients

Industry/Entity Type

earhmovibng and transport

Contact Information for Business Card

Director Name, address, email, phone number and services

Colors

Designer to choose only greyscale colors for use in the design.

Requirements
Should not have
• no yellow, red, blue or green

```html
<!DOCTYPE html>
<html lang="en">
<head>
<meta charset="utf-8">
<title>KTR Pty Ltd – Business Card</title>
<link href="https://fonts.googleapis.com/css2?family=Exo+2:ital,wght@0,800;1,700;1,800&display=swap" rel="stylesheet">
<style>
  :root{
    --stage:#c9c9cb;
    --card-black:#0d0d0e;
    --card-grey:#2c2c2f;
    --band-silver:#b4b7bb;
    --band-silver-light:#d9dbde;
    --accent-silver:#d4d6d9;
    --text-white:#f4f4f4;
    --text-dark:#111214;
    --logo-silver:#b9bcc0;
    --photo-dark:#3a3d42;
    --photo-light:#9a958c;
  }
  *{margin:0;padding:0;box-sizing:border-box}
  html,body{width:1200px;height:876px;overflow:hidden;background:var(--stage);font-family:"Exo 2",sans-serif}
  .sheet{position:relative;width:1200px;height:876px}
  .card{position:absolute;left:250px;width:700px;height:400px;border-radius:22px;overflow:hidden;
    background:radial-gradient(ellipse at 55% 30%,var(--card-grey) 0%,var(--card-black) 70%);
    box-shadow:0 10px 24px rgba(0,0,0,.25)}
  .card--front{top:22px}
  .card--back{top:454px}
  .band{position:absolute;inset:0;width:100%;height:100%}
  .photo{position:absolute;border-radius:4px;
    background:linear-gradient(160deg,var(--photo-light) 0%,var(--photo-dark) 60%,#1c1d20 100%)}
  .brand{position:absolute;display:flex;align-items:center;gap:14px;color:var(--logo-silver);
    font-weight:800;font-style:normal;letter-spacing:2px}
  .brand__mark{width:20px;height:20px;background:var(--logo-silver);border-radius:50%}
  .brand__name{font-size:40px;line-height:1}
  .contact{position:absolute;right:34px;top:112px;text-align:right;color:var(--text-white);font-style:italic;font-weight:700}
  .contact__name{color:var(--accent-silver);font-size:30px;font-weight:800;letter-spacing:1px;text-transform:uppercase}
  .contact__role{font-size:18px;margin-bottom:12px}
  .contact__line{display:flex;justify-content:flex-end;align-items:center;gap:10px;font-size:17px;line-height:28px}
  .contact__icon{width:20px;height:20px;border-radius:50%;background:var(--band-silver);display:flex;align-items:center;justify-content:center}
  .contact__icon svg{width:12px;height:12px}
  .address{position:absolute;left:30px;bottom:24px;color:var(--text-dark);font-style:italic;font-weight:700;font-size:18px}
  .services{position:absolute;left:34px;top:26px;color:var(--text-white);font-style:italic;font-weight:700}
  .services__title{color:var(--accent-silver);font-size:30px;font-weight:800;text-transform:uppercase;margin-bottom:4px}
  .services__list{list-style:none;font-size:17px;line-height:23px}
  .services__list li::before{content:"";display:inline-block;width:6px;height:6px;border-radius:50%;background:var(--band-silver);margin-right:8px;vertical-align:middle}
  .website{position:absolute;left:34px;bottom:26px;color:var(--text-dark);font-style:italic;font-weight:800;font-size:22px}
</style>
</head>
<body>
<main class="sheet">

  <section class="card card--front" aria-label="Card front">
    <svg class="band" viewBox="0 0 700 400" preserveAspectRatio="none" aria-hidden="true">
      <defs>
        <linearGradient id="silverFront" x1="0" y1="0" x2="1" y2="1">
          <stop offset="0" stop-color="var(--band-silver-light)"/>
          <stop offset="1" stop-color="var(--band-silver)"/>
        </linearGradient>
      </defs>
      <path d="M0 330 L370 330 Q410 330 440 400 L0 400 Z" fill="url(#silverFront)"/>
    </svg>
    <div class="photo" style="left:420px;top:292px;width:250px;height:108px" role="img" aria-label="Photo of a road train tanker truck"></div>
    <div class="brand" style="left:70px;top:60px">
      <span class="brand__mark"></span><span class="brand__name">KTR Pty Ltd</span>
    </div>
    <div class="contact">
      <div class="contact__name">Jonathan Smith</div>
      <div class="contact__role">Manager</div>
      <div class="contact__line">123-456-2100
        <span class="contact__icon"><svg viewBox="0 0 12 12"><path d="M2 1h3l1 3-2 1a7 7 0 0 0 3 3l1-2 3 1v3a1 1 0 0 1-1 1A10 10 0 0 1 1 2a1 1 0 0 1 1-1z" fill="#111"/></svg></span></div>
      <div class="contact__line">youremail@mailbox.com
        <span class="contact__icon"><svg viewBox="0 0 12 12"><rect x="1" y="3" width="10" height="6" fill="none" stroke="#111" stroke-width="1.4"/><path d="M1 3l5 4 5-4" fill="none" stroke="#111" stroke-width="1.4"/></svg></span></div>
      <div class="contact__line">www.yourwebsite.com
        <span class="contact__icon"><svg viewBox="0 0 12 12"><circle cx="6" cy="6" r="4.5" fill="none" stroke="#111" stroke-width="1.3"/><path d="M1.5 6h9M6 1.5c-2 2.5-2 6.5 0 9M6 1.5c2 2.5 2 6.5 0 9" fill="none" stroke="#111" stroke-width="1"/></svg></span></div>
    </div>
    <div class="address">Your address, city, state, ZIP 0000</div>
  </section>

  <section class="card card--back" aria-label="Card back">
    <svg class="band" viewBox="0 0 700 400" preserveAspectRatio="none" aria-hidden="true">
      <defs>
        <linearGradient id="silverBack" x1="0" y1="0" x2="1" y2="1">
          <stop offset="0" stop-color="var(--band-silver-light)"/>
          <stop offset="1" stop-color="var(--band-silver)"/>
        </linearGradient>
      </defs>
      <path d="M0 310 L300 310 Q350 310 390 400 L0 400 Z" fill="url(#silverBack)"/>
    </svg>
    <div class="services">
      <h2 class="services__title">Our Services</h2>
      <ul class="services__list">
        <li>Over size loads / Hot Shot Loads</li>
        <li>Road Train Tippers</li>
        <li>Heavy Vehicle Recovery Services</li>
        <li>Road Train Tankers</li>
        <li>Potable Water Del</li>
        <li>Road Train Flat Tops</li>
        <li>Road Building</li>
        <li>Road Train Tankers</li>
        <li>Potable Water Del</li>
        <li>Road Train Flat Tops</li>
      </ul>
    </div>
    <div class="photo" style="left:470px;top:200px;width:210px;height:200px" role="img" aria-label="Photo of two prime mover trucks"></div>
    <div class="brand" style="left:390px;top:130px">
      <span class="brand__mark"></span><span class="brand__name">KTR Pty Ltd</span>
    </div>
    <div class="website">www.yourwebsite.com</div>
  </section>

</main>
</body>
</html>
```